Physiotherapy Referral Pad

-Need a referral pad for physiotherapy to be provided to doctors' offices. I would like it to be simple, not too cluttered and sharp looking so doctors can quickly complete it for clients.

-I have attached my logo which I would like to include. I have also included my business cards to keep the style, font, colors etc consistent.

-I would like to include my slogan
From Our Home To Yours

-I would like it to include services options with tick boxes for Mobile, Clinic, Telehealth, KTOQFE

-I would like for it to say Call to Book or Book Online

-I would like it to include my clinic address:
427 Marden Lane
Whitehorse, YT
Y0B2K9

-I would like it to include my contact info:
Cole Pratt BSc(kin), MPT, CAFCI, IMS
(867)555-0142
physio@quarnetherapy.example

-I would like lines for the following:
Patient Name:
Diagnosis/Recommendations:
(extra lines to fill out patient info)

Physician Signature
Date

Target Market(s)

Physicians to refer clients to physiotherapy

Industry/Entity Type

Physical Therapy

Requirements
Must have
• Clean, concise, easy to look at and find pertinant categories for physicians
Nice to have
• Quarne Therapy color scheme. Please see business cards and website as needed
Should not have
• Not too cluttered or wordy

```html
<!DOCTYPE html>
<html lang="en">
<head>
<meta charset="utf-8">
<title>Quarne Therapy – Referral Pad</title>
<link href="https://fonts.googleapis.com/css2?family=Cinzel:wght@600;700&family=Roboto:wght@400&display=swap" rel="stylesheet">
<style>
  :root {
    --green: #1e5c35;
    --blue: #27388c;
    --ink: #444448;
    --rule: #6d6d72;
    --paper: #ffffff;
    --backdrop: #e6e7e9;
  }
  * { box-sizing: border-box; margin: 0; padding: 0; }
  html, body { width: 1200px; height: 1200px; overflow: hidden; background: var(--backdrop); }
  .pad {
    position: absolute; left: 242px; top: 95px; width: 714px; height: 1009px;
    background: var(--paper); font-family: 'Cinzel', Georgia, serif;
    box-shadow: 4px 4px 6px rgba(0,0,0,0.25);
  }
  .brand {
    position: absolute; left: 67px; top: 140px;
    color: var(--green); font-size: 24px; font-weight: 700; white-space: nowrap;
  }
  .contact { position: absolute; left: 421px; top: 88px; font-family: 'Roboto', Arial, sans-serif; font-size: 18px; color: var(--ink); line-height: 24px; }
  .contact-row { display: flex; align-items: center; gap: 5px; }
  .contact-icon { width: 16px; height: 16px; flex: none; }
  .provider { position: absolute; left: 0; right: 0; top: 310px; text-align: center; }
  .provider-name { color: var(--green); font-size: 34px; font-weight: 700; line-height: 40px; }
  .provider-creds { color: var(--blue); font-size: 16px; font-weight: 700; line-height: 20px; }
  .booking { color: var(--green); font-size: 21px; font-weight: 700; line-height: 30px; letter-spacing: 0.5px; }
  .services { display: flex; justify-content: center; gap: 12px; margin-top: 8px; color: var(--green); font-size: 19px; font-weight: 700; line-height: 24px; }
  .service { display: flex; align-items: center; gap: 7px; }
  .tickbox { width: 16px; height: 16px; border: 1.8px solid var(--green); }
  .field { position: absolute; left: 73px; right: 77px; display: flex; align-items: flex-end; height: 30px; color: var(--blue); font-size: 17px; font-weight: 700; }
  .field-label { margin-right: 10px; white-space: nowrap; line-height: 1; padding-bottom: 4px; }
  .field-line { flex: 1; border-bottom: 1.5px solid var(--rule); }
  .slogan-band { position: absolute; left: 0; top: 958px; width: 714px; height: 29px; }
  .slogan { position: absolute; left: 0; right: 0; top: 963px; text-align: center; color: #fff; font-size: 17px; font-weight: 600; letter-spacing: 2.5px; line-height: 20px; }
</style>
</head>
<body>
<div class="pad">
  <div class="brand">Quarne Therapy</div>

  <div class="contact">
    <div>427 Marden Lane</div>
    <div>Whitehorse, YT Y0B2K9</div>
    <div class="contact-row"><svg class="contact-icon" viewBox="0 0 20 20"><circle cx="10" cy="10" r="10" fill="var(--green)"/><path d="M6.5 5.5l2 0 1 3-1.3 1a6 6 0 0 0 2.3 2.3l1-1.3 3 1v2c0 .6-.5 1-1 1A9 9 0 0 1 5.5 6.5c0-.5.4-1 1-1z" fill="#fff"/></svg>(867)555-0142</div>
    <div class="contact-row"><svg class="contact-icon" viewBox="0 0 20 20"><rect x="3" y="5" width="14" height="10" fill="none" stroke="var(--green)" stroke-width="1.6"/><path d="M3 5l7 6 7-6" fill="none" stroke="var(--green)" stroke-width="1.6"/></svg>physio@quarnetherapy.example</div>
    <div class="contact-row"><svg class="contact-icon" viewBox="0 0 20 20"><circle cx="10" cy="10" r="10" fill="var(--green)"/><circle cx="10" cy="10" r="5" fill="none" stroke="#fff" stroke-width="1.5"/><path d="M5 10h10M10 5v10" stroke="#fff" stroke-width="1.2"/></svg>www.quarnetherapy.example</div>
  </div>

  <div class="provider">
    <div class="provider-name">COLE PRATT</div>
    <div class="provider-creds">BSc(kin), MPT, CAFCI, IMS</div>
    <div class="booking">Call to Book or Book Online</div>
    <div class="services">
      <span class="service"><span class="tickbox"></span>MOBILE</span>
      <span class="service"><span class="tickbox"></span>CLINIC</span>
      <span class="service"><span class="tickbox"></span>TELEHEALTH</span>
      <span class="service"><span class="tickbox"></span>KTOQFE</span>
    </div>
  </div>

  <div class="field" style="top:502px"><span class="field-label">PATIENT NAME:</span><span class="field-line"></span></div>
  <div class="field" style="top:563px"><span class="field-line"></span></div>
  <div class="field" style="top:622px"><span class="field-label">Diagnosis/Recommendations:</span><span class="field-line"></span></div>
  <div class="field" style="top:682px"><span class="field-line"></span></div>
  <div class="field" style="top:741px; left:77px; right:73px"><span class="field-line"></span></div>
  <div class="field" style="top:800px; left:76px"><span class="field-label">Physician Signature</span><span class="field-line"></span></div>
  <div class="field" style="top:860px; left:76px"><span class="field-label">Date</span><span class="field-line"></span></div>

  <svg class="slogan-band" viewBox="0 0 714 29" preserveAspectRatio="none">
    <rect x="0" y="0" width="714" height="29" fill="var(--green)"/>
    <polygon points="94,0 622,0 602,29 114,29" fill="var(--blue)"/>
    <polygon points="74,29 94,6 114,29" fill="var(--paper)"/>
    <polygon points="602,29 622,6 642,29" fill="var(--paper)"/>
  </svg>
  <div class="slogan">FROM OUR HOME TO YOURS</div>
</div>
</body>
</html>
```